Vitalmotion home exercise studio needs a brochure design

My problem is that I have had a fitness studio within my home for 3 years and only 2 clients per week to show for it! I need a fitness brochure designed that will literally want to make a customer pick up the phone and book a training session!

If there is any way possible to convince those exercise lovers or those who wish to become active and healthy who want to train in a private home exercise studio setting than I will be very content and happy. Obviosuly my studio within my home is not exposed to the general public and I understand that this is the reason for a shortage of clients.

I have an exercise studio with my home. It is literally the size of 6-7 x area of a standard bedroom. Most importantly, it contains the latest state of the art exercise equipment (treamills, rowers, cycle & recumberant bikes, elastic cords, bands, medballs, resistance machines, cables, squat racks, you name it..

In addition, compared to many other personal trainers out within the industry, I have clearly distinguished myself from the rest in a positive way. Firstly, I have had an extensive background as an elite athlete (NSW rowing representitive), secondly I have acquired a solid foundation of exercise science principles through 4 years of university studies (compared to most other trainers out there). Because my studio is private and obviously lacks many elements that a typical gym setting such as peak pulse, then we must be able to highlight the positives that arise from my studio compared to peak pulse or any other franchise (eg: no cancellation pollicies, no signing up for contracts, no membership fees). in addition, we must hihglight the fact that a private studio like mine will attract those who prefer not to train around others they do not know as there is no sharing of exercise equipment or duration of time one must be on a certain exercise.

We all know someone who prefers not to train in a typical gym setting where people have to compete against others for the equipment yet alone deal with the amount of starring and chatter that goes on. In addition it can get intimidating for those who prefer not many people around them. My studio is designed for any age or fitness category. In addition group training is avaliable.
In addition, I am flexible and sometimes permit going overtime for those clients who were late for there appointment. Clients that come to my home to exercise feel as if they are training within there own home rather than feeling the intimidation of going into a gym setting such as peak pulse.

If we can highlight all that has been mentioned within my brochure than thats great!

Target Market(s)

I design exercise programs and train all age groups and fitness levels

Industry/Entity Type

University

Requirements
Must have
• There must be a quote in the brochure that mentions "Together,the sky is our limit"

Must have "vitalmotion" logo

must have testimonials:

Owen -"My golf drive has increased dramatically from the use of sports specific exercises that Lachlan was able to deliver. The pain in my lower back has now ceased to flare up after a game"

Marisa - "Lachlan's knowledge and application of exercise science and health has helped me achieve a stronger and leaner body in addition to improving my 5km walking time"

Must have my qualifications:
Certificate 4 personal trainer
Diploma of fitness
Bachelor of exercise and sport science
Diploma of remedial massage
First Aid certificate

Must state that I am registered with Movement Guild

Must have that I Specialize in:

1. exercise rehabilitation
2. sport specific conditioning
3. Functional strength
4. Fat loss and toning
5. Core strength & stability
6. Flexibility
7. Cardio-respiratory fitness

Must have my mobile number: 0498 527 031
Must have my email adress: lchvorenti@mailpost-example.com.au
Nice to have
• any background images that represent motivation, will and determination.

```html
<!DOCTYPE html>
<html lang="en">
<head>
<meta charset="utf-8">
<title>Vitalmotion Brochure – Testimonials</title>
<link rel="stylesheet" href="https://fonts.googleapis.com/css2?family=Gochi+Hand&family=Open+Sans:ital,wght@0,400;0,700;1,400&family=Cinzel:wght@700&display=swap">
<style>
  :root {
    --orange: #ef7306;
    --white: #ffffff;
    --ink: #111111;
    --panel-dark: #0e1215;
    --tan: #e3a87c;
    --bar-grey: #9a9a9a;
    --brand-red: #7a1420;
    --bullet: #e0905a;
  }
  * { margin: 0; padding: 0; box-sizing: border-box; }
  html, body { width: 1200px; height: 927px; overflow: hidden; background: var(--white); }
  .brochure { position: relative; width: 1200px; height: 927px; font-family: "Open Sans", Verdana, sans-serif; color: var(--ink); }
  .shapes { position: absolute; inset: 0; }
  .testimonials-title {
    position: absolute; left: 52px; top: 18px;
    font-family: "Gochi Hand", cursive; font-size: 56px; color: var(--white); font-weight: 400; letter-spacing: 1px;
  }
  .testimonial { position: absolute; left: 30px; width: 347px; font-style: italic; font-size: 16.6px; line-height: 22.6px; letter-spacing: 0.3px; }
  .testimonial-one { top: 104px; }
  .testimonial-two { top: 258px; }
  .testimonial-author { display: block; text-align: right; font-style: normal; margin-top: 2px; }
  .specialities { position: absolute; left: 30px; top: 414px; font-size: 15px; line-height: 21px; }
  .specialities-title { font-weight: 700; font-size: 15px; }
  .specialities-list { list-style: none; }
  .studio-story { position: absolute; left: 428px; top: 40px; font-style: italic; font-size: 16.6px; line-height: 22.6px; letter-spacing: 0.3px; }
  .studio-story p + p { margin-top: 22.6px; }
  .studio-quote { font-weight: 700; }
  .qualifications { position: absolute; left: 412px; top: 546px; width: 377px; height: 286px; padding-top: 10px; }
  .qualifications-title {
    font-family: "Cinzel", Georgia, serif; color: var(--tan); text-align: center;
    font-size: 27px; line-height: 31px; font-weight: 700;
  }
  .qualifications-title span { display: block; font-size: 22px; }
  .qualification-list { list-style: none; margin: 22px 0 0 22px; }
  .qualification-list li {
    color: var(--white); font-weight: 700; font-size: 16px; line-height: 29.5px; padding-left: 16px; position: relative;
  }
  .qualification-list li::before {
    content: ""; position: absolute; left: 0; top: 12px; width: 6px; height: 6px; border-radius: 50%; background: var(--bullet);
  }
  .brand-bar {
    position: absolute; left: 412px; top: 836px; width: 377px; height: 79px;
    display: flex; flex-direction: column; align-items: center; justify-content: center; gap: 3px;
  }
  .brand-mark { display: flex; align-items: center; gap: 8px; font-weight: 700; font-size: 19px; color: var(--brand-red); }
  .brand-dot { width: 13px; height: 13px; border-radius: 50%; background: var(--brand-red); }
  .brand-contact { font-size: 11.5px; line-height: 15px; color: var(--ink); text-align: center; }
</style>
</head>
<body>
<main class="brochure">
  <svg class="shapes" width="1200" height="927" viewBox="0 0 1200 927">
    <defs>
      <linearGradient id="bodyTones" x1="0" y1="0" x2="1" y2="1">
        <stop offset="0" stop-color="#d9a68a"/><stop offset="0.6" stop-color="#c98f72"/><stop offset="1" stop-color="#5a5f66"/>
      </linearGradient>
      <linearGradient id="gymTones" x1="0" y1="0" x2="1" y2="1">
        <stop offset="0" stop-color="#c9ccd2"/><stop offset="0.55" stop-color="#8c909a"/><stop offset="1" stop-color="#3c5a9a"/>
      </linearGradient>
      <linearGradient id="beachTones" x1="0" y1="0" x2="0" y2="1">
        <stop offset="0" stop-color="#d8c9b6"/><stop offset="1" stop-color="#c4b29c"/>
      </linearGradient>
    </defs>

    <rect x="12" y="500" width="388" height="415" fill="url(#bodyTones)" role="img" aria-label="Photo of two toned fitness models' midriffs"/>
    <path d="M12,12 H400 V536 C300,580 150,640 12,721 Z" fill="var(--orange)"/>
    <path d="M12,721 C150,640 300,580 400,536" fill="none" stroke="var(--white)" stroke-width="5"/>

    <rect x="412" y="12" width="772" height="522" fill="url(#gymTones)" role="img" aria-label="Photo of the home studio with exercise balls and resistance machines"/>
    <path d="M412,12 H1100 C860,60 640,260 412,510 Z" fill="var(--orange)"/>
    <path d="M1100,12 C860,60 640,260 412,510" fill="none" stroke="var(--white)" stroke-width="5"/>

    <rect x="412" y="546" width="377" height="286" fill="var(--panel-dark)"/>
    <path d="M412,836 H789 V905 Q789,915 779,915 H422 Q412,915 412,905 Z" fill="var(--bar-grey)"/>

    <polygon points="801,536 824,492 1189,492 1189,915 801,915" fill="url(#beachTones)" role="img" aria-label="Photo of the trainer sitting on an exercise ball on the beach"/>
  </svg>

  <h1 class="testimonials-title">Testimonials</h1>

  <blockquote class="testimonial testimonial-one">
    "My golf drive has increased dramatically<br>from the use of sports specific exercises<br>that Lachlan was able to deliver. The pain<br>in my lower back has now ceased to flare<br>up after a game"
    <cite class="testimonial-author">Owen</cite>
  </blockquote>

  <blockquote class="testimonial testimonial-two">
    &nbsp;"Lachlan's knowledge and application of<br>exercise science and health has helped<br>me achieve a stronger and leaner body in<br>addition to improving my 5km walking<br>time"
    <cite class="testimonial-author">Marisa</cite>
  </blockquote>

  <section class="specialities">
    <h2 class="specialities-title">I specialise in:</h2>
    <ol class="specialities-list">
      <li>1. Exercise rehabilitation</li>
      <li>2. Sport specific conditioning</li>
      <li>3. Functional strength</li>
      <li>4. Fat loss and toning</li>
      <li>5. Core strength &amp; stability</li>
      <li>6. Flexibility</li>
      <li>7. Cardio-respiratory fitness</li>
    </ol>
  </section>

  <div class="studio-story">
    <p>Train in a private home studio with the<br>latest equipment: treadmills, rowers,<br>bikes, cables, squat racks and more. No<br>contracts, no membership fees and no<br>cancellation policies. Just you, your<br>goals and a coach who knows the science!</p>
    <p>No queues, no staring and no<br>sharing of equipment. All ages<br>and fitness levels welcome,<br>group training available.<br>Former NSW rowing rep with<br>4 years of uni study.<br><span class="studio-quote">"Together, the sky</span><br><span class="studio-quote">is our limit"</span></p>
  </div>

  <section class="qualifications">
    <h2 class="qualifications-title">Qualified Teacher<span>at your Service</span></h2>
    <ul class="qualification-list">
      <li>Certificate 4 personal trainer</li>
      <li>Diploma of fitness</li>
      <li>Bachelor of exercise and sport science</li>
      <li>Diploma of remedial massage</li>
      <li>First Aid certificate</li>
    </ul>
  </section>

  <footer class="brand-bar">
    <div class="brand-mark"><span class="brand-dot"></span>Vitalmotion</div>
    <p class="brand-contact">Registered with Movement Guild · Mobile 0498 527 031<br>lchvorenti@mailpost-example.com.au</p>
  </footer>
</main>
</body>
</html>
```